Executive search firm in fashion, luxury and retail industry needs logo and card design.

We are a start-up recruiting firm that specializes in the retail and fashion industry, based in New York. We are looking for something that will appeal to CEO level clients and candidates, but that has a little design edge...not overly corporate but still CEO-appropriate. We have clean, sophisticated taste and want a contemporary feel. Happy to have a two sided card. Not afraid of a little color but it should be high-design, not gimmicky and tasteful.

Quillmart Market(s)

CEO's, HR Leaders, in retail, fashion (i.e. Halvorsen, Quillmart, Otto Brevik)

Industry/Entity Type

Professional Service

Contact Information for Business Card

Calloway Ridge Search Partners
Address to be determined
Harrowgate, NY 10999

Marta Velard
Managing Director
(555)038-4172
mvelard@callowayridgesearch.example

Font styles to use
Serif
Sans Serif

Requirements
Must have
• clean lines, crisp graphics, some color. Prefer a graphic treatment over a "logo" per se. No pictures, etc.
Nice to have
• double sided design.
Should not have
• Gimmicks, smaltz, goop. Think Gallery of Current Works, not the Dunmore Holdings. No earth tones, as in beige and brown, no pastels. Strong colors are fine in moderation. Grays are good. Jewel tones are good. No red.

```html
<!DOCTYPE html>
<html lang="en">
<head>
<meta charset="utf-8">
<title>Calloway Ridge Search Partners — Business Card</title>
<link rel="stylesheet" href="https://fonts.googleapis.com/css2?family=Arimo:wght@400&family=Tinos:wght@700&display=swap">
<style>
  :root {
    --backdrop: #e4e4e2;
    --paper: #ffffff;
    --ink: #000000;
    --brand-blue: #087bb7;
    --on-blue: #ffffff;
  }
  * { margin: 0; padding: 0; box-sizing: border-box; }
  html, body {
    width: 1200px; height: 933px; overflow: hidden;
    background: var(--backdrop);
  }
  .canvas { position: relative; width: 1200px; height: 933px; }
  .card {
    position: absolute; left: 274px; width: 652px; height: 374px;
    overflow: hidden;
  }
  .card--front { top: 64px; background: var(--paper); }
  .card--back { top: 494px; background: var(--ink); }

  .wordmark {
    font-family: "Tinos", "Times New Roman", serif;
    font-weight: 700; font-size: 40px; letter-spacing: 0.2px;
    white-space: nowrap; text-align: center; position: absolute;
    left: 0; right: 0; line-height: 1;
  }
  .card--front .wordmark { top: 90px; transform: translateY(-50%); color: var(--ink); }
  .card--back .wordmark { top: 182px; transform: translateY(-50%); color: var(--paper); }

  .rule-band { position: absolute; left: 0; right: 0; top: 193px; height: 20px; background: var(--ink); }
  .contact-band {
    position: absolute; left: 0; right: 0; top: 213px; bottom: 0;
    background: var(--brand-blue); color: var(--on-blue);
    font-family: "Arimo", Arial, sans-serif;
  }
  .person { position: absolute; left: 36px; top: 25px; }
  .person__name { font-size: 35px; line-height: 1; font-weight: 400; }
  .person__title { font-size: 19.5px; margin-top: 14px; }
  .divider { position: absolute; left: 279px; top: 33px; width: 2px; height: 102px; background: var(--on-blue); }
  .details { position: absolute; left: 314px; top: 40px; list-style: none; }
  .details li { display: flex; align-items: center; height: 18px; margin-bottom: 18px; font-size: 16.5px; white-space: nowrap; }
  .details svg { width: 14px; height: 13px; margin-right: 16px; flex: none; }
</style>
</head>
<body>
<main class="canvas">
  <section class="card card--front">
    <h1 class="wordmark">Calloway Ridge Search Partners</h1>
    <div class="rule-band"></div>
    <div class="contact-band">
      <div class="person">
        <p class="person__name">Marta Velard</p>
        <p class="person__title">Managing Director</p>
      </div>
      <div class="divider"></div>
      <ul class="details">
        <li>
          <svg viewBox="0 0 14 13" aria-hidden="true"><rect width="14" height="13" fill="#fff"/><path d="M3 4h8v1.5H9.5V4.8h-5v.7H3z M4 6.5h6l1 3.5H3z" fill="#087bb7"/><circle cx="7" cy="8.2" r="1" fill="#fff"/></svg>
          (555)038-4172
        </li>
        <li>
          <svg viewBox="0 0 14 13" aria-hidden="true"><rect width="14" height="13" fill="#fff"/><path d="M7 2a2.6 2.6 0 0 1 2.6 2.6C9.6 6.6 7 10 7 10S4.4 6.6 4.4 4.6A2.6 2.6 0 0 1 7 2z" fill="#087bb7"/><circle cx="7" cy="4.6" r="1" fill="#fff"/></svg>
          Harrowgate, NY 10999
        </li>
        <li>
          <svg viewBox="0 0 14 13" aria-hidden="true"><rect width="14" height="13" fill="#fff"/><rect x="2.5" y="3.5" width="9" height="6" fill="none" stroke="#087bb7" stroke-width="1"/><path d="M2.5 3.5 7 7l4.5-3.5M2.5 9.5l3.2-3M11.5 9.5l-3.2-3" fill="none" stroke="#087bb7" stroke-width="1"/></svg>
          mvelard@callowayridgesearch.example
        </li>
      </ul>
    </div>
  </section>

  <section class="card card--back">
    <p class="wordmark">Calloway Ridge Search Partners</p>
  </section>
</main>
</body>
</html>
```